Home page design for a live auction website.

Hi, we are looking at finding a good design for an auction website, only home page .. We will not be selling anything online, so the website will only be a portal where visitors can check about our company, upcoming auctions, online catalogues etc.
See attached our logo. Please use the same red that you see on the logo in the designs that you provide.
The final design should communicate high-end auction website, as we will be selling expensive piece of arts and antiques.
We should have a main frame where images of arts will circulate, with description of the art piece. just like on http://paris.vellmarotte-quisande.com/
(but with a better design overall) and of course a menu with different tabs, like "about us", "previous sales" "next sales", "contact" , "how to buy", "meet our specialists".

Target Market(s)

High end segment, who can afford to pay up to 250'000 for a piece of art

Industry/Entity Type

Online

Number of Pages Required

1 page

Requirements
Must have
• a frame with images rotating, just like on http://paris.vellmarotte-quisande.com/ . but the rest of the design should be more refined.
• we should also have a strong call to action, "Free online estimation", click here, estimation delivered in 48 hours"
Nice to have
• Tremaux Auctions, the brand should be well visible

```html
<!DOCTYPE html>
<html lang="en">
<head>
<meta charset="utf-8">
<title>Tremaux Auctions</title>
<link href="https://fonts.googleapis.com/css2?family=Cinzel:wght@400;700&family=Open+Sans:wght@400;600;700&family=Great+Vibes&display=swap" rel="stylesheet">
<style>
  :root {
    --red: #c5202b;
    --red-dark: #9e1820;
    --ink: #2b2b2b;
    --text: #555555;
    --muted: #8a8a8a;
    --panel: #ececec;
    --footer: #2a2a2a;
    --white: #ffffff;
  }
  * { box-sizing: border-box; margin: 0; padding: 0; }
  html, body { width: 880px; height: 1200px; overflow: hidden; }
  body { font-family: "Open Sans", Arial, sans-serif; color: var(--text); background: var(--white); position: relative; }

  /* Header */
  .site-header { position: absolute; top: 0; left: 0; width: 880px; height: 88px; background: var(--white); }
  .brand { position: absolute; left: 34px; top: 14px; display: flex; align-items: center; gap: 10px; }
  .brand-dot { width: 30px; height: 30px; border-radius: 50%; background: var(--red); }
  .brand-name { font-family: "Cinzel", Georgia, serif; font-size: 19px; font-weight: 700; color: var(--ink); letter-spacing: 1px; }
  .contact-tab { position: absolute; right: 40px; top: 0; height: 24px; padding: 0 22px; background: var(--ink); border-radius: 0 0 14px 14px; display: flex; align-items: center; gap: 26px; color: var(--white); font-size: 11px; }
  .contact-tab span { display: flex; align-items: center; gap: 6px; }
  .main-nav { position: absolute; right: 40px; top: 50px; display: flex; gap: 0; font-size: 10.5px; font-weight: 600; color: var(--ink); text-transform: uppercase; }
  .main-nav a { color: inherit; text-decoration: none; padding: 0 9px; border-left: 1px solid #bbb; line-height: 12px; }
  .main-nav a:first-child { border-left: none; }

  /* Hero */
  .hero { position: absolute; top: 88px; left: 0; width: 880px; height: 367px; overflow: hidden; }
  .hero-photo { position: absolute; inset: 0; background: linear-gradient(100deg, #5a4a3c 0%, #8c7a66 35%, #b9a88f 60%, #6e5b49 100%); }
  .hero-shade { position: absolute; inset: 0; background: linear-gradient(90deg, rgba(0,0,0,.45) 0%, rgba(0,0,0,.15) 55%, rgba(0,0,0,.05) 100%); }
  .hero-script { position: absolute; left: 150px; top: 26px; font-family: "Great Vibes", cursive; font-size: 26px; color: var(--white); }
  .ribbon { position: absolute; left: 210px; top: 90px; height: 26px; padding: 0 22px; background: var(--red); color: var(--white); font-size: 11px; font-weight: 700; line-height: 26px; letter-spacing: 1px; }
  .hero-title { position: absolute; left: 170px; top: 130px; font-family: "Cinzel", Georgia, serif; font-size: 42px; line-height: 52px; color: var(--white); font-weight: 400; }
  .btn-register { position: absolute; left: 690px; top: 214px; height: 28px; padding: 0 22px; background: var(--red); color: var(--white); font-size: 11px; font-weight: 700; line-height: 28px; letter-spacing: 1px; border-radius: 3px; }
  .hero-arrow { position: absolute; top: 164px; width: 26px; height: 40px; background: rgba(0,0,0,.35); display: flex; align-items: center; justify-content: center; }
  .hero-arrow.prev { left: 0; }
  .hero-arrow.next { right: 0; }
  .hero-dots { position: absolute; left: 0; right: 0; bottom: 14px; display: flex; justify-content: center; gap: 7px; }
  .hero-dots i { width: 8px; height: 8px; border-radius: 50%; background: rgba(255,255,255,.6); }
  .hero-dots i.active { background: var(--red); }

  /* About */
  .about { position: absolute; top: 455px; left: 0; width: 880px; height: 265px; text-align: center; }
  .section-title { margin-top: 30px; display: flex; align-items: center; justify-content: center; gap: 16px; font-family: "Cinzel", Georgia, serif; font-size: 20px; font-weight: 700; color: var(--ink); letter-spacing: 1px; }
  .section-title::before, .section-title::after { content: ""; width: 150px; height: 1px; background: #c9c9c9; }
  .about-lead { margin: 18px auto 0; width: 680px; font-size: 13px; font-weight: 700; color: var(--red-dark); }
  .about-text { margin: 14px auto 0; width: 740px; font-size: 11px; line-height: 18px; color: var(--text); }
  .btn-read { display: inline-block; margin-top: 18px; height: 26px; padding: 0 16px; background: var(--red); color: var(--white); font-size: 11px; line-height: 26px; border-radius: 2px; }

  /* Columns */
  .features { position: absolute; top: 720px; left: 0; width: 880px; height: 350px; background: var(--panel); display: flex; gap: 30px; padding: 26px 40px 0; }
  .feature { flex: 1; }
  .feature-head { display: flex; align-items: center; gap: 10px; padding-bottom: 10px; border-bottom: 2px solid var(--red); font-family: "Cinzel", Georgia, serif; font-size: 17px; font-weight: 700; color: var(--ink); letter-spacing: .5px; }
  .item { display: flex; gap: 12px; margin-top: 16px; }
  .thumb { width: 64px; height: 50px; flex: none; background: linear-gradient(135deg, #7b6a58, #b8a68f); }
  .date { width: 50px; flex: none; text-align: center; }
  .date b { display: block; height: 32px; background: var(--white); font-size: 20px; line-height: 32px; color: var(--ink); }
  .date span { display: block; height: 20px; background: var(--ink); font-size: 11px; font-weight: 700; line-height: 20px; color: var(--white); }
  .item-title { font-size: 12px; font-weight: 700; color: var(--ink); }
  .item-text { font-size: 9.5px; line-height: 13px; color: var(--muted); margin-top: 2px; }
  .more { font-size: 9.5px; font-weight: 700; color: var(--red); margin-top: 2px; }
  .highlight-photo { margin-top: 16px; width: 100%; height: 158px; background: linear-gradient(135deg, #6b4f3a, #a7896a 55%, #5c4636); }
  .highlight-body { margin-top: 12px; }

  /* Footer */
  .site-footer { position: absolute; top: 1048px; left: 0; width: 880px; height: 152px; }
  .footer-curve { position: absolute; top: 0; left: 0; }
  .footer-inner { position: absolute; top: 22px; left: 0; right: 0; height: 130px; text-align: center; }
  .footer-brand { display: inline-flex; align-items: center; gap: 8px; margin-top: 10px; }
  .footer-brand .brand-dot { width: 22px; height: 22px; }
  .footer-brand .brand-name { font-size: 15px; color: var(--white); }
  .footer-nav { margin-top: 10px; display: flex; justify-content: center; font-size: 10px; color: #d5d5d5; }
  .footer-nav a { color: inherit; text-decoration: none; padding: 0 9px; border-left: 1px solid #666; line-height: 11px; }
  .footer-nav a:first-child { border-left: none; }
  .subscribe { margin-top: 12px; display: flex; justify-content: center; align-items: center; gap: 8px; }
  .subscribe .field { width: 200px; height: 24px; border-radius: 12px; background: var(--white); font-size: 10px; color: #999; text-align: left; padding-left: 14px; line-height: 24px; }
  .subscribe .go { height: 24px; padding: 0 14px; border-radius: 12px; background: var(--red); color: var(--white); font-size: 10px; font-weight: 700; line-height: 24px; }
  .social { width: 22px; height: 22px; border-radius: 50%; background: #555; }
  .copyright { margin-top: 10px; font-size: 9px; color: #9a9a9a; }
</style>
</head>
<body>

<header class="site-header">
  <div class="brand">
    <span class="brand-dot"></span>
    <span class="brand-name">TREMAUX AUCTIONS</span>
  </div>
  <div class="contact-tab">
    <span>
      <svg width="13" height="10" viewBox="0 0 13 10"><rect x=".5" y=".5" width="12" height="9" fill="none" stroke="#fff"/><path d="M.5 .5 6.5 5.5 12.5 .5" fill="none" stroke="#fff"/></svg>
      info@tremauxauctions.com
    </span>
    <span>
      <svg width="11" height="11" viewBox="0 0 24 24"><path fill="#fff" d="M6.6 10.8a15 15 0 0 0 6.6 6.6l2.2-2.2c.3-.3.7-.4 1-.2 1.1.4 2.3.6 3.6.6.6 0 1 .4 1 1V20c0 .6-.4 1-1 1A17 17 0 0 1 3 4c0-.6.4-1 1-1h3.5c.6 0 1 .4 1 1 0 1.2.2 2.4.6 3.6.1.3 0 .7-.2 1z"/></svg>
      555-204-7731
    </span>
  </div>
  <nav class="main-nav">
    <a>About Us</a><a>Previous Sales</a><a>Next Sales</a><a>Contact</a><a>How to Buy</a><a>Meet Our Specialists</a>
  </nav>
</header>

<section class="hero">
  <div class="hero-photo" role="img" aria-label="Gallery interior with visitors viewing framed paintings"></div>
  <div class="hero-shade"></div>
  <div class="hero-script">The Best Place To Buy And Sell</div>
  <div class="ribbon">REGISTER</div>
  <h1 class="hero-title">THE BEST PLACE<br>TO BUY AND SELL</h1>
  <div class="btn-register">REGISTER</div>
  <div class="hero-arrow prev"><svg width="10" height="14" viewBox="0 0 10 14"><path d="M8 1 2 7l6 6" fill="none" stroke="#fff" stroke-width="2"/></svg></div>
  <div class="hero-arrow next"><svg width="10" height="14" viewBox="0 0 10 14"><path d="m2 1 6 6-6 6" fill="none" stroke="#fff" stroke-width="2"/></svg></div>
  <div class="hero-dots"><i class="active"></i><i></i><i></i><i></i><i></i></div>
</section>

<section class="about">
  <h2 class="section-title">ABOUT TREMAUX AUCTIONS</h2>
  <p class="about-lead">We select and value fine art and antiques, bringing rare works to collectors.</p>
  <p class="about-text">Since our founding, our specialists have guided collectors through every step of buying and selling fine art, furniture and rare objects. Each sale is carefully prepared, every lot is researched, photographed and described with care, and our catalogues are published well in advance so that buyers can study each piece at leisure. Ask for a free estimation and receive our reply within forty-eight hours.</p>
  <div class="btn-read">Read More</div>
</section>

<section class="features">
  <div class="feature">
    <div class="feature-head">
      <svg width="14" height="16" viewBox="0 0 14 16"><rect x="0" y="0" width="3" height="16" fill="#c5202b"/><path d="M3 1h11l-3 4 3 4H3z" fill="#c5202b"/></svg>
      PREVIOUS SALES
    </div>
    <div class="item">
      <div class="thumb" role="img" aria-label="Auction room photograph"></div>
      <div><div class="item-title">Lorem ipsum dolor</div><div class="item-text">Old master paintings sold in our spring sale in Paris.</div><div class="more">Read More</div></div>
    </div>
    <div class="item">
      <div class="thumb" role="img" aria-label="Antique furniture photograph"></div>
      <div><div class="item-title">Lorem ipsum dolor</div><div class="item-text">Fine furniture and clocks from a private collection.</div><div class="more">Read More</div></div>
    </div>
    <div class="item">
      <div class="thumb" role="img" aria-label="Sculpture lot photograph"></div>
      <div><div class="item-title">Lorem ipsum dolor</div><div class="item-text">Bronze sculpture and decorative arts results.</div><div class="more">Read More</div></div>
    </div>
  </div>

  <div class="feature">
    <div class="feature-head">
      <svg width="16" height="16" viewBox="0 0 16 16"><rect x="0" y="9" width="4" height="7" fill="#c5202b"/><rect x="6" y="5" width="4" height="11" fill="#c5202b"/><rect x="12" y="1" width="4" height="15" fill="#c5202b"/></svg>
      NEXT SALES
    </div>
    <div class="item">
      <div class="date"><b>25</b><span>SEP</span></div>
      <div><div class="item-title">Lorem ipsum dolor</div><div class="item-text">Modern and contemporary art, viewing open all week.</div><div class="more">Read More</div></div>
    </div>
    <div class="item">
      <div class="date"><b>25</b><span>SEP</span></div>
      <div><div class="item-title">Lorem ipsum dolor</div><div class="item-text">Jewellery and silver, online catalogue available.</div><div class="more">Read More</div></div>
    </div>
    <div class="item">
      <div class="date"><b>20</b><span>SEP</span></div>
      <div><div class="item-title">Lorem ipsum dolor</div><div class="item-text">Asian art and ceramics, viewing by appointment.</div><div class="more">Read More</div></div>
    </div>
  </div>

  <div class="feature">
    <div class="feature-head">
      <svg width="18" height="14" viewBox="0 0 18 14"><path d="M0 7h12M8 2l5 5-5 5" fill="none" stroke="#c5202b" stroke-width="2.5"/><rect x="15" y="0" width="3" height="14" fill="#c5202b"/></svg>
      HIGH LIGHTS
    </div>
    <div class="highlight-photo" role="img" aria-label="Auction in progress with buyers in a saleroom"></div>
    <div class="highlight-body">
      <div class="item-title">Lorem ipsum dolor</div>
      <div class="item-text">A record price for a landscape painting in our latest evening sale.</div>
      <div class="more">View Details</div>
    </div>
  </div>
</section>

<footer class="site-footer">
  <svg class="footer-curve" width="880" height="152" viewBox="0 0 880 152"><path d="M0 22 Q440 -14 880 22 V152 H0 Z" fill="#2a2a2a"/></svg>
  <div class="footer-inner">
    <div class="footer-brand"><span class="brand-dot"></span><span class="brand-name">TREMAUX AUCTIONS</span></div>
    <nav class="footer-nav"><a>About Us</a><a>Previous Sales</a><a>Next Sales</a><a>Contact</a><a>How To Buy</a><a>Meet Our Specialists</a></nav>
    <div class="subscribe">
      <div class="field">Enter your email address</div>
      <div class="go">SUBSCRIBE</div>
      <span class="social"></span><span class="social"></span><span class="social"></span>
    </div>
    <div class="copyright">Copyright © 2015 Tremaux Auctions. All Rights Reserved.</div>
  </div>
</footer>

</body>
</html>
```